TV - business card

Tidewell Vantage is an insurance brokerage firm, inovative, proactive, vigorous, which aims to become the leader of the insurance brokers in Anfrica. We should like to get some designs which should be avoided also in Gray / Metallic for the Administration and Orange / Blue for the Managers (ike in the picture sent). The Blue / Green logo is not the correct one, but the source of the file. Please adjust the color accordingly for the business cards. 1 / Orange / Blue 2 / Gray / Metallic We want something classic but which is transmitted strenght, inovation, modernity and most of all, rapidity. We want something start-up like, very punchy and catching eye remaining profesional at the same time. Name: Delton Ashgrove Function: Managing Director Address: N ° 73/74 Cmt. Bolembe - R / C 2B Esquerda - Bairro Quimbuta - Luanda Tel: (+244) 947 385 619 Email: delton.ashgrove@tidewell-v.com Website: www.tidewell-v. com We want classic in the front and creative, colorfull at the back. The cards will be printed in relief, with very high quality of paper.
Industry/Entity Type
Insurance Broker
Colors
Designer to choose colors to be used in the design.
Look and feel

```html
<!DOCTYPE html>
<html lang="en">
<head>
<meta charset="utf-8">
<title>Tidewell Vantage – Business Card</title>
<link rel="stylesheet" href="https://fonts.googleapis.com/css2?family=Titillium+Web:wght@400;600&display=swap">
<style>
  :root {
    --paper: #f5f5f5;
    --ink: #141414;
    --brand-orange: #f26531;
    --brand-blue: #1a97c4;
  }
  html, body {
    margin: 0;
    padding: 0;
    width: 796px;
    height: 1200px;
    overflow: hidden;
    background: var(--paper);
  }
  .card {
    position: relative;
    width: 796px;
    height: 1200px;
    background: var(--paper);
    color: var(--ink);
    font-family: "Titillium Web", sans-serif;
    overflow: hidden;
  }
  .person-name {
    position: absolute;
    left: 78px;
    top: 82px;
    margin: 0;
    font-size: 72px;
    font-weight: 600;
    line-height: 1;
    letter-spacing: 0.5px;
  }
  .person-role {
    position: absolute;
    left: 84px;
    top: 190px;
    margin: 0;
    font-size: 50px;
    font-weight: 400;
    line-height: 1;
  }
  .contact {
    position: absolute;
    left: 80px;
    margin: 0;
    font-size: 48px;
    font-weight: 400;
    line-height: 66px;
    font-style: normal;
  }
  .contact-address { top: 302px; }
  .contact-phone { top: 556px; }
  .contact-email { top: 676px; font-size: 45px; }
  .contact-web {
    top: 800px;
    left: auto;
    right: 52px;
  }
  .brand-mark {
    position: absolute;
    left: 0;
    bottom: 0;
    width: 796px;
    height: 360px;
  }
  .brand-circle {
    position: absolute;
    left: -150px;
    bottom: -150px;
    width: 400px;
    height: 400px;
    border-radius: 50%;
    background: var(--brand-orange);
  }
  .brand-name {
    position: absolute;
    left: 290px;
    bottom: 90px;
    margin: 0;
    font-size: 54px;
    font-weight: 600;
    line-height: 1;
    color: var(--brand-blue);
  }
</style>
</head>
<body>
  <main class="card">
    <h1 class="person-name">Delton Ashgrove</h1>
    <p class="person-role">Managing Director</p>

    <address class="contact contact-address">
      N° 73/74 Cmt. Bolembe -<br>
      R / C 2B Esquerda -<br>
      Bairro Quimbuta - Luanda
    </address>

    <p class="contact contact-phone">(+244) 947 385 619</p>
    <p class="contact contact-email">delton.ashgrove@tidewell-v.com</p>
    <p class="contact contact-web">www.tidewell-v. com</p>

    <div class="brand-mark">
      <div class="brand-circle"></div>
      <p class="brand-name">Tidewell Vantage</p>
    </div>
  </main>
</body>
</html>
```